Marigold comb home studio

MARIGOLD COMB.....at fox valley ,Wahroonga is a home hairdressing studio.
Hair services from a peaceful setting.
Quality colours and products.
free consultation prior to making appointment.
Easy and convenient after hours hair appointments.
Qualified hairdresser with over 15 years experience.
Specialise in foiling,balayage,ombre colour,tints,style cutting and blowdrying.
20 % off for new clients(colour services)
sms or call for 0493620174 for a quote.
Updates
im sorry guys but i has to re do alot of the photos. i would like something that looks elegant and classy.i will post an example of a flier style i like Added Wednesday, April 27, 2016
Project Deadline Extended Reason: im sorry i have decided i needed better photographs. please design again...i will choose someone before the deadline. please an elegant design will be great Added Wednesday, April 27, 2016
Target Market(s)
18-60 year olds
Industry/Entity Type
Hair
Requirements
Must have
- Must say home hairdressing studio
- Must say Marigold Comb at Fox Valley Wahroonga
- Must say phone number
Nice to have
- Modern but still classy and elegant
- Try to incorporate any photos which I have uploaded that looks best

```html
<!DOCTYPE html>
<html lang="en">
<head>
<meta charset="utf-8">
<title>Marigold Comb — Home hairdressing studio</title>
<link rel="stylesheet" href="https://fonts.googleapis.com/css2?family=Tinos:ital,wght@0,400;0,700;1,400;1,700&family=Pinyon+Script&display=swap">
<style>
  :root {
    --page: #ffffff;
    --paper-mid: #dedde1;
    --paper-light: #e8e6e8;
    --ink: #1c1a1c;
    --house-sky: #a9bcd6;
    --house-roof: #8d8079;
    --house-brick: #82685b;
    --house-garden: #8f9a6a;
    --house-lawn: #8ea76a;
    --salon-wall-top: #f1e6dc;
    --salon-wall: #eadbcf;
    --salon-floor: #dcbf9f;
    --salon-floor-deep: #d3b08b;
  }
  * { box-sizing: border-box; margin: 0; padding: 0; }
  html, body {
    width: 1200px; height: 1014px; overflow: hidden;
    background: var(--page);
  }
  .flyer {
    position: absolute; left: 30px; top: 104px;
    width: 1140px; height: 806px; overflow: hidden;
    background: linear-gradient(90deg, var(--paper-mid), var(--paper-light) 60%, var(--salon-wall));
    font-family: "Tinos", "Times New Roman", serif;
    color: var(--ink);
  }
  .photo { position: absolute; top: 0; bottom: 0; }
  .photo-house {
    left: 0; width: 620px;
    background: linear-gradient(180deg,
      var(--house-sky) 0%, var(--house-roof) 16%, var(--house-brick) 36%,
      var(--house-brick) 55%, var(--house-garden) 72%, var(--house-lawn) 100%);
    -webkit-mask-image: linear-gradient(90deg, #000 35%, rgba(0,0,0,.55) 62%, transparent 100%);
            mask-image: linear-gradient(90deg, #000 35%, rgba(0,0,0,.55) 62%, transparent 100%);
    opacity: .9;
  }
  .photo-salon {
    right: 0; width: 440px;
    background: linear-gradient(180deg,
      var(--salon-wall-top) 0%, var(--salon-wall) 70%,
      var(--salon-floor) 80%, var(--salon-floor-deep) 100%);
    -webkit-mask-image: linear-gradient(90deg, transparent 0%, #000 40%);
            mask-image: linear-gradient(90deg, transparent 0%, #000 40%);
  }
  .content { position: absolute; inset: 0; text-align: center; }
  .line { position: absolute; left: 0; right: 0; white-space: nowrap; }
  .title { top: 78px; font-style: italic; font-weight: 400; font-size: 37px; }
  .business { top: 128px; font-size: 25px; }
  .business .name { font-family: "Pinyon Script", cursive; font-size: 46px; }
  .features { top: 238px; right: 20px; font-style: italic; font-size: 22px; line-height: 32.5px; }
  .features li { list-style: none; }
  .offer { top: 492px; left: 14px; font-style: italic; font-size: 62px; }
  .offer-note { top: 574px; left: 2px; font-family: "Pinyon Script", cursive; font-size: 31px; }
  .contact { top: 678px; font-style: italic; font-size: 29px; }
  .contact b { font-weight: 700; }
</style>
</head>
<body>
  <main class="flyer">
    <div class="photo photo-house" role="img" aria-label="Photo of a two-storey brick house with lawn and garden stones"></div>
    <div class="photo photo-salon" role="img" aria-label="Photo of the studio interior with framed mirror and styling chair"></div>
    <div class="content">
      <h1 class="line title">Home hairdressing studio</h1>
      <p class="line business"><span class="name">Marigold Comb</span> at Fox Valley, Wahroonga</p>
      <ul class="line features">
        <li>~ Hair services from a peaceful setting</li>
        <li>~ Quality colours and products</li>
        <li>~ Free consultation prior to making appointment</li>
        <li>~ Easy and convenient after hours hair appointments</li>
        <li>~ Qualified hairdresser with over 15 years experience</li>
        <li>~ Specialise in foiling,balayage,ombre colour,tints,style cutting and blowdrying</li>
      </ul>
      <p class="line offer">20 % off</p>
      <p class="line offer-note">for new clients(colour services)</p>
      <p class="line contact">sms or call <b>0493620174</b> for a quote</p>
    </div>
  </main>
</body>
</html>
```